Labels for an activated Charcoal Facial Wash, Scrub and Mask

We need a new label design for a new line of Facial products. The product, falls under our Brand Lumivo and is based on Activated Charcoal. Activated Black Charcoal Facial wash (250ml), Activated Black Charcoal Mask (100gms) and Activated Black Charcoal face scrub (100gms). We would like to see designs that are modern, clean and must communicate natural products.

```html
<!DOCTYPE html>
<html lang="en">
<head>
<meta charset="utf-8">
<title>Lumivo Activated Charcoal Labels</title>
<link href="https://fonts.googleapis.com/css2?family=Raleway:wght@300;400&display=swap" rel="stylesheet">
<style>
  :root {
    --backdrop: #e4e4e4;
    --label-black: #141414;
    --label-white: #f1f1f2;
    --cream: #dcd9b9;
    --cream-dark: #8a8766;
    --silver: #b9babd;
    --smoke-tone: #cbcbcd;
    --leaf-tone: #e9e7da;
  }
  * { margin: 0; padding: 0; box-sizing: border-box; }
  html, body { width: 1200px; height: 964px; overflow: hidden; }
  body {
    background: var(--backdrop);
    font-family: "Raleway", sans-serif;
    font-weight: 300;
    color: var(--cream);
    position: relative;
  }
  .label { position: absolute; overflow: hidden; box-shadow: 0 6px 18px rgba(0,0,0,0.12); }

  .art-placeholder { position: absolute; }
  .smoke-art { background: var(--smoke-tone); }
  .leaf-art { background: var(--leaf-tone); }

  /* Facial wash tube label */
  .tube-label { left: 70px; top: 110px; width: 300px; height: 720px; background: var(--label-black); }
  .tube-label .top-band { position: absolute; left: 0; top: 0; width: 100%; height: 250px; background: var(--label-white); }
  .tube-label .silver-rule { position: absolute; left: 0; top: 26px; width: 100%; height: 3px; background: var(--silver); }
  .tube-label .smoke-art { right: 0; top: 36px; width: 130px; height: 120px; }
  .tube-label .leaf-art { left: 24px; top: 120px; width: 50px; height: 110px; }
  .tube-label .leaf-art.right { left: auto; right: 24px; top: 180px; width: 70px; height: 56px; }

  .product-copy { text-align: center; }
  .product-copy p { white-space: nowrap; }
  .product-copy .kicker { letter-spacing: 0.3px; }
  .product-copy .main { font-weight: 400; letter-spacing: 0.5px; line-height: 1.1; }
  .product-copy .type { letter-spacing: 0.5px; line-height: 1.15; }
  .size { text-align: center; font-weight: 400; }

  .tube-label .product-copy { position: absolute; top: 282px; width: 100%; }
  .tube-label .product-copy .kicker { font-size: 15px; }
  .tube-label .product-copy .main { font-size: 33px; }
  .tube-label .product-copy .type { font-size: 26px; }

  .brand-box {
    position: absolute; left: 50%; transform: translateX(-50%);
    border: 1px solid var(--cream);
    display: flex; flex-direction: column; align-items: center; justify-content: flex-end;
  }
  .brand-mark { background: var(--cream); }
  .brand-name { font-weight: 400; color: var(--cream); }
  .tube-label .brand-box { top: 415px; width: 134px; height: 102px; padding-bottom: 12px; }
  .tube-label .brand-mark { width: 12px; height: 12px; margin-bottom: 22px; }
  .tube-label .brand-name { font-size: 17px; letter-spacing: 6px; }
  .tube-label .size { position: absolute; top: 662px; width: 100%; font-size: 12px; }
  .cream-rule { position: absolute; left: 0; width: 100%; background: var(--cream); }
  .tube-label .cream-rule { top: 694px; height: 2px; }

  /* Jar labels */
  .jar-label { top: 424px; width: 296px; height: 190px; background: var(--label-black); }
  .jar-label.mask { left: 494px; }
  .jar-label.scrub { left: 830px; }
  .jar-label .top-band { position: absolute; left: 0; top: 0; width: 100%; height: 62px; background: var(--label-white); }
  .jar-label .silver-rule { position: absolute; left: 0; top: 5px; width: 100%; height: 2px; background: var(--silver); }
  .jar-label .smoke-art { right: 0; top: 8px; width: 26px; height: 44px; }
  .jar-label .leaf-art { left: 12px; top: 10px; width: 44px; height: 20px; }
  .jar-label .leaf-art.right { left: auto; right: 40px; top: 30px; width: 50px; height: 28px; }
  .jar-label .brand-box { top: 14px; width: 66px; height: 44px; padding-bottom: 4px; }
  .jar-label .brand-mark { width: 6px; height: 6px; margin-bottom: 8px; background: var(--cream-dark); }
  .jar-label .brand-name { font-size: 8px; letter-spacing: 2.5px; color: var(--cream-dark); }
  .jar-label .product-copy { position: absolute; top: 80px; width: 100%; }
  .jar-label .product-copy .kicker { font-size: 12px; }
  .jar-label .product-copy .main { font-size: 27px; }
  .jar-label .product-copy .type { font-size: 21px; }
  .jar-label .size { position: absolute; top: 164px; width: 100%; font-size: 9px; }
  .jar-label .cream-rule { top: 180px; height: 2px; }
</style>
</head>
<body>

<section class="label tube-label">
  <div class="top-band">
    <div class="silver-rule"></div>
    <div class="art-placeholder smoke-art" role="img" aria-label="Charcoal powder burst illustration"></div>
    <div class="art-placeholder leaf-art" role="img" aria-label="Fine line botanical leaf sprig"></div>
    <div class="art-placeholder leaf-art right" role="img" aria-label="Fine line botanical leaves"></div>
  </div>
  <div class="product-copy">
    <p class="kicker">ACTIVATED BLACK</p>
    <p class="main">CHARCOAL</p>
    <p class="type">FACIAL WASH</p>
  </div>
  <div class="brand-box">
    <span class="brand-mark"></span>
    <span class="brand-name">LUMIVO</span>
  </div>
  <p class="size">250ml/8.5oz</p>
  <div class="cream-rule"></div>
</section>

<section class="label jar-label mask">
  <div class="top-band">
    <div class="silver-rule"></div>
    <div class="art-placeholder leaf-art" role="img" aria-label="Fine line botanical leaf sprig"></div>
    <div class="art-placeholder leaf-art right" role="img" aria-label="Fine line botanical leaves"></div>
    <div class="art-placeholder smoke-art" role="img" aria-label="Charcoal powder burst illustration"></div>
    <div class="brand-box">
      <span class="brand-mark"></span>
      <span class="brand-name">LUMIVO</span>
    </div>
  </div>
  <div class="product-copy">
    <p class="kicker">ACTIVATED BLACK</p>
    <p class="main">CHARCOAL</p>
    <p class="type">FACIAL MASK</p>
  </div>
  <p class="size">100gm/3.5oz</p>
  <div class="cream-rule"></div>
</section>

<section class="label jar-label scrub">
  <div class="top-band">
    <div class="silver-rule"></div>
    <div class="art-placeholder leaf-art" role="img" aria-label="Fine line botanical leaf sprig"></div>
    <div class="art-placeholder leaf-art right" role="img" aria-label="Fine line botanical leaves"></div>
    <div class="art-placeholder smoke-art" role="img" aria-label="Charcoal powder burst illustration"></div>
    <div class="brand-box">
      <span class="brand-mark"></span>
      <span class="brand-name">LUMIVO</span>
    </div>
  </div>
  <div class="product-copy">
    <p class="kicker">ACTIVATED BLACK</p>
    <p class="main">CHARCOAL</p>
    <p class="type">FACIAL SCRUB</p>
  </div>
  <p class="size">100gm/3.5oz</p>
  <div class="cream-rule"></div>
</section>

</body>
</html>
```